Theatre company seeking web designer/programmer

We are a theatre company re-branding and looking for a web programmer to build the site we have designed. We are an outside the box theatre company and have designed an a-typical website for ourselves. We need a programmer comfortable with HTML5 to build the site and its limited but important animation.

There should be about 5 pages themselves- most incredibly simple and we essentially have them designed already. We need someone who can build what we have designed, and program the small amount of animation we have.

I have a video attached to this project showing the landing page and home page. The animation on the landing page is the most complicated the site gets. I have the other pages designed as well and can send along to the person selected for this project.

We also hope to keep a working, project-by-project relationship with our designer/programmer, as updates for the site come up (For additional project-by project funding.)

Industry/Entity Type

It Company

Coding

Coded - Design and coding required

Number of Pages Required

5+ page

Colors
ec1f27
ffcf3e
0255a3
000000
ffffff

Requirements
Must have
• The ability to program our animation.
Nice to have
• A desire to work with us again in the future as we need updates to the site.

```html
<!DOCTYPE html>
<html lang="en">
<head>
<meta charset="utf-8">
<title>The Outsider Guild</title>
<link rel="stylesheet" href="https://fonts.googleapis.com/css2?family=Audiowide&family=Roboto:wght@300;400;700&display=swap">
<style>
  :root {
    --red: #ec1f27;
    --white: #ffffff;
    --black: #000000;
    --grey: #8a8a8a;
    --smoke-1: #2a2826;
    --smoke-2: #141312;
  }
  * { margin: 0; padding: 0; box-sizing: border-box; }
  html, body { width: 1200px; height: 818px; overflow: hidden; background: var(--black); }
  body { position: relative; font-family: "Roboto", sans-serif; color: var(--white); }

  .hero { position: absolute; left: 0; top: 0; width: 1200px; height: 677px; }
  .hero-backdrop {
    position: absolute; inset: 0;
    background:
      radial-gradient(ellipse 520px 260px at 600px 300px, var(--smoke-1) 0%, rgba(30,28,26,0) 100%),
      radial-gradient(ellipse at center, var(--smoke-2) 0%, #080808 100%);
  }

  .menu-toggle { position: absolute; left: 1077px; top: 81px; width: 23px; height: 20px; }

  .brand {
    position: absolute; left: 0; top: 114px; width: 1200px; text-align: center;
    font-weight: 700; font-size: 38px; letter-spacing: 3px; text-transform: uppercase; color: var(--red);
  }

  .main-nav a {
    position: absolute; top: 182px; font-size: 22px; letter-spacing: 1.5px; color: var(--white);
    text-decoration: underline; text-underline-offset: 4px; text-decoration-thickness: 1px; transform: translateX(-50%);
    white-space: nowrap;
  }
  .main-nav .about { left: 434px; }
  .main-nav .members { left: 773px; }

  .event { position: absolute; left: 0; width: 1200px; text-align: center; }
  .event-date { top: 365px; font-weight: 300; font-size: 36px; letter-spacing: 2px; }
  .event-title { top: 413px; font-family: "Audiowide", sans-serif; font-size: 33px; color: var(--red); text-transform: uppercase; letter-spacing: 1px; }
  .event-subtitle { top: 462px; font-weight: 300; font-size: 22px; letter-spacing: 2px; text-transform: uppercase; }

  .join-button {
    position: absolute; left: 537px; top: 518px; width: 147px; height: 61px;
    border: 1.5px solid var(--red); color: var(--red); text-decoration: none;
    display: flex; align-items: center; justify-content: center;
    font-weight: 300; font-size: 23px; letter-spacing: 1.5px;
  }

  .site-footer { position: absolute; left: 0; top: 677px; width: 1200px; height: 141px; background: var(--black); }
  .social-links { position: absolute; top: 43px; left: 0; width: 1200px; height: 27px; }
  .social-links a {
    position: absolute; top: 0; width: 27px; height: 27px; border: 1px solid var(--white);
    display: flex; align-items: center; justify-content: center;
  }
  .social-links a span { width: 7px; height: 7px; background: var(--red); }
  .copyright {
    position: absolute; top: 92px; left: 0; width: 1200px; text-align: center;
    font-size: 12.5px; color: var(--grey);
  }
  .page-code { position: absolute; left: 1105px; top: 88px; font-size: 12px; color: var(--white); }
</style>
</head>
<body>
  <header class="hero">
    <div class="hero-backdrop" role="img" aria-label="Dark smoky grunge photograph of a shadowy ruin behind the headline"></div>

    <svg class="menu-toggle" viewBox="0 0 23 20" aria-label="Menu">
      <rect x="0" y="0" width="23" height="4" fill="var(--white)"/>
      <rect x="0" y="8" width="23" height="4" fill="var(--white)"/>
      <rect x="0" y="16" width="23" height="4" fill="var(--white)"/>
    </svg>

    <div class="brand">The Outsider Guild</div>

    <nav class="main-nav">
      <a class="about" href="#">ABOUT MEMBERS</a>
      <a class="members" href="#">MEMBERS ONLY</a>
    </nav>

    <p class="event event-date">May 1961</p>
    <h1 class="event event-title">The Summer I Disappeared</h1>
    <p class="event event-subtitle">A Beat Poetry Salon Hosted by Marian Holloway &amp; TOG</p>

    <a class="join-button" href="#">JOIN US</a>
  </header>

  <footer class="site-footer">
    <div class="social-links">
      <a href="#" style="left:527px" aria-label="Social profile one"><span></span></a>
      <a href="#" style="left:566px" aria-label="Social profile two"><span></span></a>
      <a href="#" style="left:606px" aria-label="Social profile three"><span></span></a>
      <a href="#" style="left:646px" aria-label="Social profile four"><span></span></a>
    </div>
    <p class="copyright">Copyright © 2015 theoutsiderguild. All rights reserved.</p>
    <span class="page-code">C 19</span>
  </footer>
</body>
</html>
```